KTR Associates Business Card

I would like to have a business card designed that uses my current logo and colors. I am not looking for anything to "out there" but can have a little fun so that it stands out.

I have a boutique consulting firm that specializes in strategic planning, change management, leadership development and innovation.

Industry/Entity Type

Leadership

Contact Information for Business Card

Marta Holbeck
President
marta@ktr-associates.example
555-014-2286

```html
<!DOCTYPE html>
<html lang="en">
<head>
<meta charset="utf-8">
<title>KTR Associates – Business Card</title>
<link rel="stylesheet" href="https://fonts.googleapis.com/css2?family=Arimo:wght@400&family=Roboto+Condensed:wght@700&display=swap">
<style>
  :root {
    --card-black: #000000;
    --card-edge: #3a3a3a;
    --logo-white: #ffffff;
    --name-light: #e6e6e6;
    --detail-grey: #9a9a9a;
    --band-deep: #127a12;
    --band-mid: #5fb83a;
    --band-light: #e2ff78;
  }
  html, body {
    margin: 0;
    padding: 0;
    width: 706px;
    height: 1200px;
    overflow: hidden;
    background: var(--card-black);
  }
  .card {
    position: relative;
    width: 706px;
    height: 1200px;
    box-sizing: border-box;
    background: var(--card-black);
    border: 1px solid var(--card-edge);
    overflow: hidden;
    font-family: "Arimo", Arial, sans-serif;
  }
  .wordmark {
    position: absolute;
    top: 170px;
    left: 0;
    width: 100%;
    margin: 0;
    text-align: center;
    font-family: "Arimo", Arial, sans-serif;
    font-weight: 400;
    font-size: 84px;
    line-height: 1;
    color: var(--logo-white);
  }
  .holder-name {
    position: absolute;
    top: 682px;
    left: 166px;
    margin: 0;
    font-family: "Roboto Condensed", "Arial Narrow", sans-serif;
    font-weight: 700;
    font-size: 43px;
    line-height: 1;
    color: var(--name-light);
  }
  .details {
    position: absolute;
    top: 882px;
    left: 167px;
    margin: 0;
    padding: 0;
    list-style: none;
    font-size: 29px;
    line-height: 37px;
    color: var(--detail-grey);
    white-space: nowrap;
  }
  .details .indent { padding-left: 2px; }
  .accent-band {
    position: absolute;
    left: 0;
    bottom: 0;
    width: 100%;
    height: 28px;
    background: linear-gradient(90deg, var(--band-deep) 0%, var(--band-mid) 40%, var(--band-light) 100%);
  }
</style>
</head>
<body>
  <main class="card">
    <h1 class="wordmark">KTR Associates</h1>

    <p class="holder-name">MARTA HOLBECK</p>

    <ul class="details">
      <li>President</li>
      <li>Strategic Planning</li>
      <li>Change Management</li>
      <li class="indent">Leadership Development</li>
      <li class="indent">Innovation</li>
      <li class="indent">Tel: 555-014-2286</li>
      <li class="indent">marta@ktr-associates.example</li>
    </ul>

    <div class="accent-band"></div>
  </main>
</body>
</html>
```